We need to a website for a contact center that provides answering services by voice and chat.

A similar website in terms of design is the following site:
http://www.brindlecallhub.net/

The colors and look and feel should be different and creative but the structure should be similar to the above mentioned website.

Attached is the text file.

The design should communicate professionalism and friendly customer service oriented company. The visitor to the site must have a feel that "this company looks professional and they will take care of my client."

I am looking for design only, but if the designer will also do the coding, it will be an advantage.

Target Market(s)

Our target market are lawyers and doctors who require someone to answer their clients calls 24/7.

Industry/Entity Type

It Company

Requirements
Nice to have
• Since the company is based in Dubai, the website should reflect the Middle East people not pure European or pure Asians. A mixture of nationalities is fine to be visible in the pictures but it must include at least an arab or middle eastern person.
Should not have
• No old style, Times Roman font, do not include illustrations or cartoon graphics or pictures that are very common or widely used.

```html
<!DOCTYPE html>
<html lang="en">
<head>
<meta charset="utf-8">
<title>Brindle Call Hub – Premium Live Receptionist</title>
<link rel="stylesheet" href="https://fonts.googleapis.com/css2?family=Arimo:wght@400;700&family=Raleway:wght@400;600;700&family=Roboto+Condensed:wght@400;700;900&family=Ubuntu:wght@400;500&display=swap">
<style>
:root{
  --teal:#0e6b6b;
  --teal-deep:#0a4f52;
  --teal-light:#2a9a94;
  --gold:#c0862a;
  --gold-bright:#d9a441;
  --ink:#1d2424;
  --sand-band:#f5efe4;
  --sand-line:#e4d9c4;
  --footer:#1c2b2c;
  --footer-text:#b9c6c4;
  --footer-head:#ffffff;
  --icon-bg:#3f5556;
}
*{margin:0;padding:0;box-sizing:border-box}
html,body{width:984px;height:1200px;overflow:hidden;background:#fff}
body{position:relative;font-family:"Arimo",Arial,sans-serif;color:var(--ink)}
.abs{position:absolute}

/* header */
.site-header{position:absolute;left:0;top:0;width:984px;height:75px;background:#fff}
.brand{position:absolute;left:144px;top:18px;display:flex;align-items:center;gap:8px;font-family:"Roboto Condensed",sans-serif;font-weight:900;font-size:24px;color:var(--teal);letter-spacing:.3px}
.brand-dot{width:17px;height:17px;border-radius:50%;background:var(--gold)}
.main-nav{position:absolute;top:52px;left:0;font-family:"Roboto Condensed",sans-serif;font-size:12px;color:#243030}
.main-nav a{position:absolute;white-space:nowrap;color:inherit;text-decoration:none;padding-bottom:7px}
.main-nav a.active{border-bottom:3px solid var(--gold);color:var(--teal)}

/* hero */
.hero{position:absolute;left:0;top:75px;width:984px;height:327px;overflow:hidden}
.hero-photo{position:absolute;inset:0;background:linear-gradient(180deg,#f3e6cf 0%,#ead6b4 55%,#d9bf94 100%)}
.hero-person{position:absolute;left:470px;top:18px;width:350px;height:309px;border-radius:160px 160px 0 0;background:linear-gradient(180deg,rgba(58,46,38,.55) 0%,#2f3a3d 45%,#243033 100%)}
.hero-title{position:absolute;left:150px;top:47px;font-family:"Roboto Condensed",sans-serif;font-weight:900;font-size:37px;color:var(--teal-deep);letter-spacing:.3px}
.hero-sub{position:absolute;left:150px;top:93px;font-family:"Roboto Condensed",sans-serif;font-size:18px;color:var(--gold)}
.hero-list{position:absolute;left:151px;top:127px;list-style:none;font-family:"Raleway",sans-serif;font-size:11px;color:#1d2424}
.hero-list li{height:22.5px}

/* about */
.about-title{position:absolute;left:141px;top:426px;font-family:"Roboto Condensed",sans-serif;font-size:23px;font-weight:400;color:var(--teal)}
.about-text{position:absolute;left:142px;top:459px;width:466px;font-size:9.2px;line-height:16.8px;color:#1d2424}
.about-text p+p{margin-top:16.8px}
.about-text .more{color:var(--gold);font-weight:700}
.video{position:absolute;left:626px;top:436px;width:216px;height:154px;border:2px solid var(--sand-line);background:linear-gradient(135deg,#efe2c9,#cdb189 60%,#8e7a5e)}
.video-bar{position:absolute;left:4px;right:4px;bottom:4px;height:20px;background:rgba(16,40,41,.85)}
.video-play{position:absolute;left:8px;top:5px}
.video-time{position:absolute;left:42px;bottom:25px;background:#fff;font-size:7px;padding:1px 3px;color:#222}
.video-side{position:absolute;right:8px;width:26px;height:21px;background:rgba(16,40,41,.85);border-radius:2px}

/* features */
.features{position:absolute;left:0;top:625px;width:984px;height:230px;background:var(--sand-band);border-top:1px solid var(--sand-line)}
.feature{position:absolute;top:34px;width:200px;text-align:center}
.feature-circle{margin:0 auto;width:106px;height:106px;border-radius:50%;background:radial-gradient(circle at 45% 35%,var(--teal-light),var(--teal-deep) 78%);border:3px solid #fff;box-shadow:0 0 0 1px #d3c6ad;display:flex;align-items:center;justify-content:center}
.feature-title{margin-top:12px;font-family:"Ubuntu",sans-serif;font-weight:500;font-size:15px;color:var(--gold);letter-spacing:.5px}
.feature-text{margin-top:3px;font-family:"Ubuntu",sans-serif;font-size:9.5px;line-height:14px;color:#1d2424}

/* footer */
.site-footer{position:absolute;left:0;top:855px;width:984px;height:345px;background:var(--footer);font-family:"Raleway",sans-serif;color:var(--footer-text)}
.f-head{position:absolute;font-weight:700;font-size:10.5px;color:var(--footer-head)}
.f-links{position:absolute;list-style:none;font-size:9.5px}
.f-links li{height:17.6px}
.f-about{position:absolute;left:334px;top:43px;width:258px;font-size:8.8px;line-height:14.7px}
.contact-row{position:absolute;left:628px;display:flex;align-items:center;gap:7px;font-family:"Roboto Condensed",sans-serif;font-size:14.5px;color:#fff}
.contact-row .label{color:#8fa3a1}
.c-icon{width:30px;height:30px;border-radius:50%;background:var(--icon-bg);display:flex;align-items:center;justify-content:center}
.footer-brand{position:absolute;left:700px;top:182px;display:flex;align-items:center;gap:6px;font-family:"Roboto Condensed",sans-serif;font-weight:900;font-size:19px;color:#d8cfbd}
.footer-brand .dot{width:13px;height:13px;background:var(--gold);border-radius:50%}
.rule{position:absolute;left:148px;width:694px;height:1px;background:#3a4c4d}
.newsletter{position:absolute;left:148px;top:243px;display:flex;align-items:center;font-size:13px;color:#fff}
.newsletter strong{margin:0 4px 0 8px}
.news-input{position:absolute;left:486px;top:248px;width:126px;height:21px;background:#fff;border-radius:2px;font-size:9px;color:#888;padding:5px 7px}
.news-btn{position:absolute;left:616px;top:248px;width:59px;height:21px;background:var(--gold-bright);border-radius:2px;color:#1c2b2c;font-weight:700;font-size:12px;text-align:center;line-height:21px}
.social{position:absolute;top:244px;width:30px;height:30px;border-radius:50%;background:var(--icon-bg)}
.legal{position:absolute;left:147px;top:304px;font-size:9.2px;line-height:17px}
.legal-links{position:absolute;right:145px;top:320px;font-size:9.2px}
.c-glyph{fill:#d9a441}
</style>
</head>
<body>

<header class="site-header">
  <div class="brand"><span class="brand-dot"></span>Brindle Call Hub</div>
  <nav class="main-nav">
    <a class="active" style="left:330px">How It Works</a>
    <a style="left:421px">Industries</a>
    <a style="left:494px">About Us</a>
    <a style="left:569px">Testimonials</a>
    <a style="left:658px">Pricing</a>
    <a style="left:721px">Press Room</a>
    <a style="left:807px">Contact</a>
  </nav>
</header>

<section class="hero">
  <div class="hero-photo" role="img" aria-label="Soft-focus Dubai skyline at golden hour behind the receptionist"></div>
  <div class="hero-person" role="img" aria-label="Smiling Middle Eastern receptionist in a dark suit gesturing towards the text"></div>
  <h1 class="hero-title">Premium Live Receptionist.</h1>
  <p class="hero-sub">Rouite Your Business Calls to Any Location.</p>
  <ul class="hero-list">
    <li>US Based Receptionists</li>
    <li>Bilingual English/Spanish Speaking Receptionists</li>
    <li>Free Trial, No Credit Card</li>
    <li>Affordable Prices</li>
    <li>Local or Toll Free Number Available</li>
  </ul>
</section>

<section>
  <h2 class="about-title">About Brindle Call Hub.</h2>
  <div class="about-text">
    <p>Brindle Call Hub is a 24/7 business call center and live answering service that provides customized solutions for small, medium, and large businesses. Our clients capture more leads and increase revenues by pre-senting a professional company image for their customers, while saving them thousands of dollars on overhead and labor costs simply dummy text of the printing and typesetting industry.</p>
    <p>Lorem Ipsum has been the industry's standard dummy text ever since the 1500s, when an unknown printer took a galley of type and scrambled it to make a type specimen book. It has survived not only saving them thousands of dollars on overhead five centuries, <span class="more">Read More</span>.</p>
  </div>
  <div class="video" role="img" aria-label="Video still of an Arab and an Asian colleague working together at a laptop">
    <div class="video-side" style="top:22px"></div>
    <div class="video-side" style="top:46px"></div>
    <div class="video-side" style="top:70px"></div>
    <span class="video-time">03:12</span>
    <div class="video-bar">
      <svg class="video-play" width="12" height="10" viewBox="0 0 12 10"><path d="M1 0 L11 5 L1 10Z" fill="#fff"/></svg>
    </div>
  </div>
</section>

<section class="features">
  <div class="feature" style="left:153px">
    <div class="feature-circle">
      <svg width="56" height="56" viewBox="0 0 56 56" fill="none" stroke="#fff" stroke-width="4"><circle cx="28" cy="28" r="25"/><path d="M14 34 V28 a14 14 0 0 1 28 0 V34"/><rect x="13" y="30" width="6" height="10" rx="2" fill="#fff"/><rect x="37" y="30" width="6" height="10" rx="2" fill="#fff"/></svg>
    </div>
    <div class="feature-title">Listen to a Live Demo</div>
    <div class="feature-text">Brindle Call Hub is business<br>call center and live answering service</div>
  </div>
  <div class="feature" style="left:391px">
    <div class="feature-circle">
      <svg width="56" height="56" viewBox="0 0 56 56"><rect x="4" y="4" width="48" height="48" fill="#0f5e60"/><path d="M18 12 H40 V40 L32 46 H18 V36" fill="none" stroke="#fff" stroke-width="3"/><path d="M12 38 L32 22 L36 27 L16 43Z" fill="#fff"/></svg>
    </div>
    <div class="feature-title">Request Pricing</div>
    <div class="feature-text">Brindle Call Hub is business<br>call center and live answering service</div>
  </div>
  <div class="feature" style="left:624px">
    <div class="feature-circle">
      <svg width="56" height="56" viewBox="0 0 56 56"><ellipse cx="22" cy="34" rx="13" ry="15" transform="rotate(-35 22 34)" fill="#fff"/><path d="M28 24 C32 14 44 22 40 10 C38 4 48 4 46 12" fill="none" stroke="#fff" stroke-width="3"/><path d="M14 28 L24 38" stroke="#1a7f7c" stroke-width="2"/></svg>
    </div>
    <div class="feature-title">Online Signup</div>
    <div class="feature-text">Brindle Call Hub is business<br>call center and live answering service</div>
  </div>
</section>

<footer class="site-footer">
  <div class="f-head" style="left:148px;top:20px">LATEST NEWS</div>
  <ul class="f-links" style="left:148px;top:42px">
    <li>CONFERENCE SCHEDULE</li>
    <li>GENERAL INFORMATION</li>
    <li>NEW - VIGA Vision Statement</li>
  </ul>
  <div class="f-head" style="left:148px;top:111px">POPULAR</div>
  <ul class="f-links" style="left:148px;top:133px">
    <li>Inspection FAQs</li>
    <li>Common Venting of Gas Appliances</li>
    <li>Becoming a Member</li>
    <li>Education / CECs</li>
    <li>Affiliate Directory</li>
  </ul>

  <div class="f-head" style="left:334px;top:20px">WHO ARE WE?</div>
  <p class="f-about">Established in 1976, VIGA is a non-profit trade association, with chapters located throughout the state. VIGA is a member-driven, hands-on organization that provides educational programming and on-going opportunities for its members to interact at both local and statewide VIGA meetings and events.</p>

  <div class="contact-row" style="top:19px">
    <span class="c-icon"><svg width="16" height="14" viewBox="0 0 16 14"><path class="c-glyph" d="M0 5 H9 V1 L16 7 L9 13 V9 H0Z"/></svg></span>
    <span>REQUEST A QUOTE</span>
  </div>
  <div class="contact-row" style="top:62px">
    <span class="c-icon"><svg width="16" height="12" viewBox="0 0 16 12" fill="none" stroke="#d9a441" stroke-width="1.6"><rect x="1" y="1" width="14" height="10"/><path d="M1 1 L8 7 L15 1"/></svg></span>
    <span><span class="label">EMAIL US: </span>INFO@BCH.NET</span>
  </div>
  <div class="abs" style="left:678px;top:88px;font-family:'Roboto Condensed',sans-serif;font-size:14.5px;color:#fff">info@brindlecallhub.net</div>
  <div class="contact-row" style="top:117px">
    <span class="c-icon"><svg width="15" height="15" viewBox="0 0 24 24"><path class="c-glyph" d="M6.6 10.8a15 15 0 0 0 6.6 6.6l2.2-2.2a1 1 0 0 1 1-.25 11.4 11.4 0 0 0 3.6.57 1 1 0 0 1 1 1V20a1 1 0 0 1-1 1A17 17 0 0 1 3 4a1 1 0 0 1 1-1h3.5a1 1 0 0 1 1 1c0 1.25.2 2.45.57 3.57a1 1 0 0 1-.25 1z"/></svg></span>
    <span><span class="label">CALL US ON: </span>1.800.555.0142</span>
  </div>
  <div class="footer-brand"><span class="dot"></span>Brindle Call Hub</div>

  <div class="rule" style="top:230px"></div>
  <div class="newsletter">
    <span class="c-icon"><svg width="16" height="12" viewBox="0 0 16 12" fill="none" stroke="#d9a441" stroke-width="1.6"><rect x="1" y="1" width="14" height="10"/><path d="M1 1 L8 7 L15 1"/></svg></span>
    <strong>Newsletter</strong>Stay up to date with our latest news
  </div>
  <div class="news-input">Email Address</div>
  <div class="news-btn">Sign Up</div>
  <div class="social" style="left:769px"></div>
  <div class="social" style="left:806px"></div>
  <div class="rule" style="top:288px"></div>

  <div class="legal">418 Linden Avenue&nbsp; Suite 12, Maple Ridge CA 95000-1200 | Hours: M-F, 8:00am - 5:00pm<br>©2013 Brindle Call Hub. ALL Rights Reserved. Privacy Policy | Terms of Service</div>
  <div class="legal-links">About VIGA &nbsp;|&nbsp; News &nbsp;|&nbsp; Privacy/Security/Terms</div>
</footer>

</body>
</html>
```